Personal training and nutrition business needs business card design

We need a business card that outlays our services and invites potential customers to join our team and take the first step to a healthier and more enjoyable life. We cater for any level of fitness and specialize in weight loss and conditioning, strength training, muscle gain and strength endurance. Whether you are just starting off or need some help getting to the next level of your journey we are here to get the job done.
We specialize in one on one or one on two personal training sessions and each program will be custom made to suit individual fitness goals of our clients

```html
<!DOCTYPE html>
<html lang="en">
<head>
<meta charset="utf-8">
<title>Stride &amp; Forge — Business Card</title>
<link href="https://fonts.googleapis.com/css2?family=Poppins:wght@300;400;600;800&family=Russo+One&display=swap" rel="stylesheet">
<style>
  :root{
    --ink:#050505;
    --paper:#ffffff;
    --violet:#7449a3;
    --orchid:#b062b0;
    --purple:#9457a8;
    --pink:#c267bf;
    --text:#1d1d1f;
    --stage:#2a2a2c;
  }
  *{box-sizing:border-box;margin:0;padding:0}
  html,body{width:1200px;height:900px;overflow:hidden}
  body{background:var(--stage);font-family:'Poppins',sans-serif;position:relative}

  .card{position:absolute;left:250px;width:700px;height:400px;overflow:hidden;box-shadow:0 10px 30px rgba(0,0,0,.45)}
  .card--front{top:30px}
  .card--back{top:470px}
  .card svg.card__art{position:absolute;inset:0;width:700px;height:400px}

  .brand{position:absolute;display:flex;flex-direction:column;align-items:flex-start}
  .brand__row{display:flex;align-items:center;gap:12px}
  .brand__dot{width:22px;height:22px;border-radius:50%;background:var(--purple)}
  .brand__name{font-family:'Poppins',sans-serif;font-weight:800;font-size:34px;letter-spacing:1px;line-height:1.05;text-transform:uppercase}
  .brand__tagline{margin-top:8px;font-family:'Poppins',sans-serif;font-weight:600;font-size:10px;letter-spacing:1px;color:var(--pink);text-transform:uppercase}

  .card--front .brand{left:40px;top:150px}
  .card--front .brand__name{color:var(--paper)}

  .name-pill{position:absolute;left:420px;top:48px;width:300px;height:66px;border-radius:33px;background:var(--purple);padding:8px 0 0 34px;color:var(--paper)}
  .name-pill__name{font-size:30px;line-height:1.05;font-weight:300}
  .name-pill__name strong{font-weight:600}
  .name-pill__role{font-size:11px;font-weight:400;margin-left:120px}

  .contacts{position:absolute;right:28px;top:138px;list-style:none;text-align:right;font-size:14px;color:var(--text)}
  .contacts li{display:flex;justify-content:flex-end;align-items:center;gap:12px;height:28px}
  .contacts .icon{width:18px;height:18px;border-radius:50%;background:var(--purple);display:flex;align-items:center;justify-content:center}
  .contacts .icon svg{width:10px;height:10px}
  .address{position:absolute;right:58px;top:242px;text-align:right;font-size:13px;line-height:1.5;color:var(--text)}

  .card--back .brand{left:60px;top:120px}
  .card--back .brand__name{color:var(--ink)}
  .web-pill{position:absolute;left:60px;top:318px;width:320px;height:48px;border-radius:24px;background:var(--purple);color:var(--paper);font-size:20px;display:flex;align-items:center;justify-content:center;letter-spacing:.5px}

  .specialties{position:absolute;right:24px;top:50px;text-align:right}
  .specialties__title{font-family:'Russo One',sans-serif;font-size:22px;color:var(--violet);letter-spacing:1px;margin-bottom:14px;font-weight:400}
  .specialties ul{list-style:none}
  .specialties li{font-size:14px;color:var(--pink);display:flex;justify-content:flex-end;align-items:center;gap:14px;height:28px}
  .specialties li::after{content:"";width:9px;height:9px;border-radius:50%;background:var(--pink)}
</style>
</head>
<body>

<section class="card card--front" aria-label="Business card front">
  <svg class="card__art" viewBox="0 0 700 400" aria-hidden="true">
    <defs>
      <linearGradient id="paperFade" x1="0" y1="0" x2="0" y2="1">
        <stop offset="0" stop-color="#ffffff"/><stop offset="1" stop-color="#e8e7ea"/>
      </linearGradient>
    </defs>
    <rect width="700" height="400" fill="url(#paperFade)"/>
    <path d="M0,0 L350,0 C380,200 430,340 490,400 L0,400 Z" fill="var(--orchid)"/>
    <path d="M0,0 L325,0 C355,200 405,340 465,400 L0,400 Z" fill="var(--violet)"/>
    <path d="M0,0 L300,0 C330,200 380,340 440,400 L0,400 Z" fill="var(--ink)"/>
  </svg>

  <div class="brand">
    <div class="brand__row"><span class="brand__dot"></span><span class="brand__name">Stride<br>&amp; Forge</span></div>
    <span class="brand__tagline">Personal Training. Nutrition. Motivation</span>
  </div>

  <div class="name-pill">
    <div class="name-pill__name">Owen <strong>Hale</strong></div>
    <div class="name-pill__role">Gym Instructor</div>
  </div>

  <ul class="contacts">
    <li>+12 3456 7890<span class="icon"><svg viewBox="0 0 10 10"><path d="M2 1 L4 1 L4.6 3 L3.6 3.8 Q4.6 5.6 6.2 6.4 L7 5.4 L9 6 L9 8 Q5 9 1.5 4.5 Q1 2.5 2 1Z" fill="#fff"/></svg></span></li>
    <li>info@yourwebsite.com<span class="icon"><svg viewBox="0 0 10 10"><rect x="1" y="2.5" width="8" height="5.5" fill="none" stroke="#fff" stroke-width="1"/><path d="M1 2.5 L5 5.5 L9 2.5" fill="none" stroke="#fff" stroke-width="1"/></svg></span></li>
    <li>www.yourwebsite.com<span class="icon"><svg viewBox="0 0 10 10"><circle cx="5" cy="5" r="4" fill="none" stroke="#fff" stroke-width="1"/><path d="M1 5 H9 M5 1 Q2.5 5 5 9 M5 1 Q7.5 5 5 9" fill="none" stroke="#fff" stroke-width=".8"/></svg></span></li>
  </ul>
  <p class="address">Dummy Street Address, Room No,<br>New York 112052</p>
</section>

<section class="card card--back" aria-label="Business card back">
  <svg class="card__art" viewBox="0 0 700 400" aria-hidden="true">
    <rect width="700" height="400" fill="var(--paper)"/>
    <path d="M0,325 L520,325 L540,368 L0,368 Z" fill="var(--purple)"/>
    <path d="M330,0 L700,0 L700,400 L550,400 C450,340 370,180 330,0 Z" fill="var(--orchid)"/>
    <path d="M355,0 L700,0 L700,400 L575,400 C475,340 395,180 355,0 Z" fill="var(--violet)"/>
    <path d="M380,0 L700,0 L700,400 L600,400 C500,340 420,180 380,0 Z" fill="var(--ink)"/>
  </svg>

  <div class="brand">
    <div class="brand__row"><span class="brand__dot"></span><span class="brand__name">Stride<br>&amp; Forge</span></div>
    <span class="brand__tagline">Personal Training. Nutrition. Motivation</span>
  </div>

  <div class="web-pill">www.yourwebsite.com</div>

  <div class="specialties">
    <h2 class="specialties__title">OUR SPECILIZATION</h2>
    <ul>
      <li>Fitness Training</li>
      <li>Weight loss &amp; Conditioning</li>
      <li>Strength Training</li>
      <li>Muscle Gain</li>
      <li>&amp; Strength Endurance</li>
    </ul>
  </div>
</section>

</body>
</html>
```